Anatomic 3D models + Urological Robotic surgery site

I want a website to represent my business as a developer of 3D models (reconstructions based on CT and MRI scans) and urological robotic surgery. The main point I need on my website is that it is modern, very attractive, clean, responsive and an interaction that differentiate me from the usual websites they have in my market. The site will be in portuguese and I'll provide the content to be used. The company name would be my name: Dr Mateus Vilhena. The colors and other choices I made here are not final decisions. If you have a suggestion you, they are welcome.

Target Market(s)

My patients

Industry/Entity Type

Medical

Coding

Number of Pages Required

1 page

Font styles to use
Sans Serif

Colors
0054AA
0677BA
7BADD7
CADEEF
E8F1F8
0094D4
00A9DD
6FCCEA
C7EBF8
E9F6FB
00AB8E
00BBA5
67D7C9
C6EFE9
E9F9F6
59FF00
82FF00
B8FF75
E3FFCB
F4FFEA
FFC000
F8CF3A
FAE287
FDF2CF
FEFAEE
F0912C
F2A743
F7CA91
FBE8D2
FDF5EE
A7469A
B969AE
D3A5CF
EDDBEB
F8F0F9
6B429C
8869AF
B7A5CE
E3DAEB
F3F0F8

Requirements
Must have
• Responsive, clean, modern, attractive, stand out from usual sites.
Should not have
• Antiquate boring designs.

```html
<!DOCTYPE html>
<html lang="en">
<head>
<meta charset="utf-8">
<title>Dr. Mateus Vilhena — Robotic Urology</title>
<link rel="stylesheet" href="https://fonts.googleapis.com/css2?family=Poppins:wght@400;500;600;700&family=Montserrat:wght@400;500;600&display=swap">
<style>
:root{
  --blue:#0b6fbf;
  --blue-dark:#0a5fa6;
  --ink:#111418;
  --text:#2b2f36;
  --muted:#555b64;
  --soft:#f2f2f2;
  --white:#ffffff;
  --icon-soft:#e3eef8;
}
*{box-sizing:border-box;margin:0;padding:0}
html,body{width:1200px;height:4468px;overflow:hidden}
body{font-family:"Montserrat",sans-serif;color:var(--text);background:var(--white);position:relative}
h1,h2,h3,.display{font-family:"Poppins",sans-serif}
.section{position:absolute;left:0;width:1200px}
.abs{position:absolute}
.eyebrow{font-family:"Poppins",sans-serif;color:var(--blue);font-size:15px;font-weight:500;letter-spacing:.2px;text-transform:uppercase}
.title{font-family:"Poppins",sans-serif;font-weight:700;font-size:28px;color:var(--ink);text-transform:uppercase;line-height:1.18}
.copy{font-size:11.5px;line-height:19.5px;color:var(--text)}
.center{text-align:center;left:0;width:1200px}

/* button */
.btn{position:absolute;display:flex;align-items:center;justify-content:space-between;height:35px;padding:0 4px 0 20px;border-radius:18px;background:var(--blue);color:var(--white);font-family:"Poppins",sans-serif;font-weight:600;font-size:11px;text-transform:uppercase;text-decoration:none}
.btn .arrow{width:27px;height:27px;border-radius:50%;background:var(--white);display:flex;align-items:center;justify-content:center}
.btn.outline .arrow{border:2px solid var(--blue)}

/* header */
.site-header{top:0;height:81px;background:var(--white)}
.brand{position:absolute;display:flex;align-items:center;gap:10px;font-family:"Poppins",sans-serif;font-weight:500;font-size:14px;color:var(--ink)}
.brand .dot{width:40px;height:40px;border-radius:50%;background:var(--blue)}
.nav a{position:absolute;top:32px;font-family:"Poppins",sans-serif;font-weight:500;font-size:11.5px;color:var(--ink);text-decoration:none}

/* hero */
.hero{top:81px;height:512px;background:linear-gradient(90deg,#3d6f9c 0%,#5c88b0 35%,#7ea3c2 55%,#9fb9cf 75%,#8aa5bf 100%)}
.hero h1{position:absolute;left:99px;top:103px;width:420px;color:var(--white);font-weight:700;font-size:35px;line-height:45px}
.hero p{position:absolute;left:99px;top:253px;width:380px;color:var(--white);font-size:14px;line-height:21px}
.hero-photo{position:absolute;left:470px;top:0;width:730px;height:512px;background:linear-gradient(100deg,rgba(140,170,200,0) 0%,rgba(150,180,205,.55) 25%,rgba(90,140,190,.6) 60%,rgba(60,110,170,.7) 100%)}
.hero-badge{position:absolute;left:565px;top:475px;width:70px;height:70px;border-radius:50%;background:var(--white);box-shadow:0 6px 18px rgba(0,0,0,.12);display:flex;align-items:center;justify-content:center}

/* about */
.about{top:593px;height:602px}
.about-photo{position:absolute;left:156px;top:128px;width:418px;height:401px;border-radius:22px 22px 22px 140px;background:linear-gradient(160deg,#9ec2d6 0%,#cfe0ea 45%,#eef3f6 100%);box-shadow:0 10px 30px rgba(0,0,0,.15)}
.about .copy{font-size:11.5px;line-height:19px;letter-spacing:.2px}

/* approach */
.approach{top:1195px;height:550px;background:var(--soft)}
.card{position:absolute;background:var(--white);border-radius:22px;box-shadow:0 6px 22px rgba(0,0,0,.06);text-align:center;font-family:"Poppins",sans-serif;font-weight:500;font-size:13px;line-height:21px;color:var(--ink)}
.icon-circle{position:absolute;width:84px;height:84px;border-radius:50%;background:var(--blue);display:flex;align-items:center;justify-content:center}

/* planning */
.planning{top:1745px;height:578px}
.planning-photo{position:absolute;left:602px;top:81px;width:452px;height:415px;border-radius:34px 34px 120px 120px;background:linear-gradient(170deg,#d9e2ea 0%,#8fb0cc 40%,#5a87b2 75%,#3f6f9f 100%)}

/* support */
.support{top:2323px;height:455px;background:var(--soft)}
.support-photo{position:absolute;left:0;top:0;width:600px;height:455px;background:linear-gradient(135deg,#35679a 0%,#8fa9c3 45%,#c9d4df 70%,#8ba3bd 100%)}
.ticks li{list-style:none;display:flex;align-items:center;gap:6px;font-size:11.5px;color:var(--text);height:24px}

/* postoperative */
.postop{top:2778px;height:473px}
.card.feature{background:var(--blue);color:var(--white)}
.soft-circle{position:absolute;width:84px;height:84px;border-radius:50%;background:var(--icon-soft);display:flex;align-items:center;justify-content:center}

/* commitment */
.commitment{top:3251px;height:325px;background:linear-gradient(90deg,#1b2533 0%,#2c3a4d 40%,#3a4c63 65%,#1e2836 100%)}
.commitment .eyebrow,.commitment .title,.commitment .copy{color:var(--white)}

/* contact */
.contact{top:3576px;height:568px}
.contact-card{position:absolute;left:277px;top:79px;width:656px;height:470px;background:var(--white);border-top:5px solid var(--blue);border-radius:12px 12px 0 0;box-shadow:0 8px 28px rgba(0,0,0,.08)}
.field{position:absolute;height:36px;border:1px solid #d6d9de;border-radius:3px;display:flex;align-items:center;font-size:10px;color:#444}
.field .ico{width:34px;height:100%;display:flex;align-items:center;justify-content:center;border-right:1px solid #d6d9de;margin-right:10px}
.field.tall{align-items:flex-start;height:73px}
.field.tall .ico{height:34px}
.field.tall span{padding-top:11px}

/* footer */
.site-footer{top:4144px;height:324px;background:var(--blue)}
.site-footer .brand{color:var(--white);font-size:17px}
.site-footer .brand .dot{background:var(--white)}
.foot-nav{position:absolute;top:150px;left:0;width:1200px;display:flex;justify-content:center;gap:26px}
.foot-nav a{color:var(--white);text-decoration:none;font-family:"Poppins",sans-serif;font-size:11px;font-weight:500}
.info{position:absolute;top:193px;display:flex;align-items:center;gap:14px;color:var(--white)}
.info .ring{width:34px;height:34px;border-radius:50%;background:rgba(255,255,255,.2);display:flex;align-items:center;justify-content:center}
.info b{display:block;font-family:"Poppins",sans-serif;font-size:11px;font-weight:600}
.info span{font-size:11px}
.divider{position:absolute;top:193px;width:1px;height:34px;background:rgba(255,255,255,.3)}
.copyright{position:absolute;top:292px;left:0;width:1200px;text-align:center;color:var(--white);font-size:11px}
.foot-rule{position:absolute;top:268px;left:0;width:1200px;height:1px;background:rgba(255,255,255,.25)}
</style>
</head>
<body>

<header class="section site-header">
  <div class="brand" style="left:100px;top:20px"><span class="dot"></span>DR. MATEUS VILHENA</div>
  <nav class="nav">
    <a style="left:343px" href="#">Home</a>
    <a style="left:397px" href="#">About</a>
    <a style="left:451px" href="#">Our Approach</a>
    <a style="left:550px" href="#">3D Planning</a>
    <a style="left:636px" href="#">Pre-Procedure</a>
    <a style="left:739px" href="#">Postoperative Care</a>
    <a style="left:865px" href="#">Our Commitment</a>
  </nav>
  <a class="btn" href="#" style="left:981px;top:21px;width:117px;height:38px;border-radius:19px"><span>Contact</span><span class="arrow"><svg width="12" height="12" viewBox="0 0 12 12"><path d="M3 9L9 3M4.5 3H9v4.5" stroke="#0b6fbf" stroke-width="1.4" fill="none"/></svg></span></a>
</header>

<section class="section hero">
  <div class="hero-photo" role="img" aria-label="Surgical team operating with a robotic surgery system"></div>
  <h1>Caring with Precision, Treating with Empathy</h1>
  <p>Advanced robotic surgery and comprehensive patient care tailored to your needs.</p>
  <a class="btn outline" href="#" style="left:99px;top:314px;width:139px"><span>Get in touch</span><span class="arrow"><svg width="12" height="12" viewBox="0 0 12 12"><path d="M3 9L9 3M4.5 3H9v4.5" stroke="#0b6fbf" stroke-width="1.4" fill="none"/></svg></span></a>
  <div class="hero-badge"><svg width="22" height="30" viewBox="0 0 22 30"><rect x="2" y="2" width="18" height="26" rx="9" fill="none" stroke="#0b6fbf" stroke-width="2"/><path d="M11 9v10M8 16l3 3 3-3" stroke="#0b6fbf" stroke-width="1.8" fill="none"/></svg></div>
</section>

<section class="section about">
  <div class="about-photo" role="img" aria-label="Portrait of the urologist in a white coat with a stethoscope"></div>
  <div class="abs eyebrow" style="left:633px;top:172px">About</div>
  <h2 class="abs title" style="left:633px;top:194px">Dr. Mateus Vilhena</h2>
  <p class="abs copy" style="left:633px;top:233px;width:420px">I am a urologist specializing in robotic surgery and comprehensive patient care. My approach combines cutting-edge technology with attentive listening to deliver treatments grounded in science and empathy.</p>
  <p class="abs copy" style="left:633px;top:318px;width:420px">My mission is to respect each patient's unique needs, offering personalized care that prioritizes your health, choices, and goals.</p>
  <p class="abs copy" style="left:633px;top:364px;width:420px">Lorem ipsum dolor sit amet, consectetuer adicing elit sed diam nonummy nibh euismod tincidunt ut laoreet dolore magna aliquam erat volutpat. Ut wisi enim ad minim veniam quis nostrud exerci tation.</p>
  <a class="btn outline" href="#" style="left:633px;top:446px;width:123px"><span>About me</span><span class="arrow"><svg width="12" height="12" viewBox="0 0 12 12"><path d="M3 9L9 3M4.5 3H9v4.5" stroke="#0b6fbf" stroke-width="1.4" fill="none"/></svg></span></a>
</section>

<section class="section approach">
  <div class="abs eyebrow center" style="top:76px">How we operate</div>
  <h2 class="abs title center" style="top:100px">Our Approach</h2>
  <p class="abs copy center" style="top:137px">Not every treatment needs to be surgical. Not every surgery needs to be robotic.</p>
  <p class="abs copy center" style="top:160px">Robotic surgery is a great advance, but it must be indicated with criteria. Before proposing any intervention, we evaluate the case broadly:</p>

  <div class="card" style="left:151px;top:237px;width:279px;height:168px"><div style="padding-top:70px">We use the most<br>up-to-date medical guidelines</div></div>
  <div class="icon-circle" style="left:248px;top:203px"><svg width="38" height="38" viewBox="0 0 38 38" fill="none" stroke="#fff" stroke-width="1.8"><rect x="8" y="6" width="22" height="27" rx="2"/><rect x="14" y="3" width="10" height="6" rx="1.5"/><path d="M13 16h12M13 21h12M13 26h8"/></svg></div>

  <div class="card" style="left:461px;top:237px;width:279px;height:168px"><div style="padding-top:70px">We make use of artificial<br>intelligence tools to support<br>clinical decision-making</div></div>
  <div class="icon-circle" style="left:559px;top:203px"><svg width="40" height="40" viewBox="0 0 40 40" fill="none" stroke="#fff" stroke-width="1.8"><circle cx="20" cy="20" r="11"/><ellipse cx="20" cy="20" rx="17" ry="7"/><text x="20" y="24" fill="#fff" stroke="none" font-family="Poppins,sans-serif" font-size="10" font-weight="600" text-anchor="middle">AI</text></svg></div>

  <div class="card" style="left:775px;top:237px;width:279px;height:168px"><div style="padding-top:70px">We conduct frank conversations<br>about the real needs, benefits<br>and risks of each approach.</div></div>
  <div class="icon-circle" style="left:872px;top:203px"><svg width="38" height="38" viewBox="0 0 38 38" fill="none" stroke="#fff" stroke-width="1.8"><circle cx="19" cy="19" r="6"/><path d="M19 5v5M19 28v5M5 19h5M28 19h5M9 9l3.5 3.5M25.5 25.5L29 29M29 9l-3.5 3.5M12.5 25.5L9 29"/></svg></div>

  <p class="abs copy center" style="top:445px">Our focus is to ensure that the patient is referred to the option with the greatest potential for outcome</p>
  <p class="abs copy center" style="top:465px">be it surgical, clinical, or even active surveillance.</p>
</section>

<section class="section planning">
  <div class="abs eyebrow" style="left:149px;top:166px">Technology</div>
  <h2 class="abs title" style="left:149px;top:190px;width:360px">Planning with 3D Technology</h2>
  <p class="abs copy" style="left:149px;top:264px;width:420px">Using personalized 3D models created from your exams, we plan kidney and prostate surgeries with unmatched precision.</p>
  <p class="abs copy" style="left:149px;top:312px;width:420px">This approach reduces bleeding, shortens surgical time, and improves outcomes, often altering the strategy in nearly half of cases.</p>
  <a class="btn outline" href="#" style="left:149px;top:374px;width:174px"><span>See how it works</span><span class="arrow"><svg width="12" height="12" viewBox="0 0 12 12"><path d="M3 9L9 3M4.5 3H9v4.5" stroke="#0b6fbf" stroke-width="1.4" fill="none"/></svg></span></a>
  <div class="planning-photo" role="img" aria-label="Surgeons in blue scrubs performing a procedure in an operating room"></div>
</section>

<section class="section support">
  <div class="support-photo" role="img" aria-label="Nurse reviewing a tablet with a patient resting in a hospital bed"></div>
  <div class="abs eyebrow" style="left:649px;top:116px">Support</div>
  <h2 class="abs title" style="left:649px;top:140px">Pre-Procedure Support</h2>
  <p class="abs copy" style="left:649px;top:185px;width:410px">We handle the details so you can focus on your health. Our dedicated team offers:</p>
  <ul class="abs ticks" style="left:649px;top:231px">
    <li><svg width="11" height="11" viewBox="0 0 11 11"><circle cx="5.5" cy="5.5" r="4.6" fill="none" stroke="#0b6fbf" stroke-width="1.3"/><path d="M3.3 5.6l1.5 1.5 3-3" stroke="#0b6fbf" stroke-width="1.3" fill="none"/></svg>Streamlined coordination with hospitals and health plans</li>
    <li><svg width="11" height="11" viewBox="0 0 11 11"><circle cx="5.5" cy="5.5" r="4.6" fill="none" stroke="#0b6fbf" stroke-width="1.3"/><path d="M3.3 5.6l1.5 1.5 3-3" stroke="#0b6fbf" stroke-width="1.3" fill="none"/></svg>Close, human support to ease your preparation</li>
  </ul>
  <a class="btn outline" href="#" style="left:649px;top:297px;width:175px"><span>Talk to our team</span><span class="arrow"><svg width="12" height="12" viewBox="0 0 12 12"><path d="M3 9L9 3M4.5 3H9v4.5" stroke="#0b6fbf" stroke-width="1.4" fill="none"/></svg></span></a>
</section>

<section class="section postop">
  <div class="abs eyebrow center" style="top:86px">Care and recovery</div>
  <h2 class="abs title center" style="top:110px">Postoperative Care</h2>
  <p class="abs copy center" style="top:144px">Recovery is a critical part of your journey. Our team provides:</p>

  <div class="card" style="left:151px;top:180px;width:279px;height:210px"><div style="padding-top:142px">Home visits by nurses and<br>physiotherapists</div></div>
  <div class="soft-circle" style="left:248px;top:213px"><svg width="38" height="38" viewBox="0 0 38 38" fill="none" stroke="#0b6fbf" stroke-width="1.8"><circle cx="19" cy="13" r="6"/><path d="M8 33c0-7 5-11 11-11s11 4 11 11"/><path d="M16 27h6M19 24v6"/></svg></div>

  <div class="card feature" style="left:461px;top:180px;width:279px;height:210px"><div style="padding-top:142px">Guidance on movement,<br>nutrition, and medications</div></div>
  <div class="soft-circle" style="left:559px;top:213px;background:#fff"><svg width="40" height="40" viewBox="0 0 40 40" fill="none" stroke="#0b6fbf" stroke-width="1.8"><path d="M5 26l7-4h8a2 2 0 010 4h-6M5 32l9-2 12-6 6-3a2 2 0 00-2-3l-8 4"/><circle cx="26" cy="12" r="7"/><path d="M26 8v8M22 12h8"/></svg></div>

  <div class="card" style="left:775px;top:180px;width:279px;height:210px"><div style="padding-top:142px">Direct contact for ongoing<br>support and monitoring</div></div>
  <div class="soft-circle" style="left:872px;top:213px"><svg width="40" height="40" viewBox="0 0 40 40" fill="none" stroke="#0b6fbf" stroke-width="1.8"><rect x="6" y="9" width="24" height="17" rx="2"/><path d="M12 32h12M18 26v6M10 18h5l2-4 3 8 2-4h4"/><circle cx="30" cy="11" r="5"/><path d="M28 11l1.5 1.5L32 10"/></svg></div>
</section>

<section class="section commitment">
  <div style="position:absolute;inset:0;background:rgba(15,22,32,.25)" role="img" aria-label="Doctor talking with a patient in a clinic, darkened backdrop"></div>
  <div class="abs eyebrow center" style="top:81px;text-transform:uppercase">Dedicated to your care</div>
  <h2 class="abs title center" style="top:105px">Our Commitment</h2>
  <p class="abs copy center" style="top:143px">We combine knowledge, technology, and empathy to deeply understand your needs and build the best treatment path together.</p>
  <p class="abs copy center" style="top:166px">Every patient is unique—and deserves care that reflects that.</p>
  <a class="btn outline" href="#" style="left:529px;top:206px;width:139px"><span>Get in touch</span><span class="arrow"><svg width="12" height="12" viewBox="0 0 12 12"><path d="M3 9L9 3M4.5 3H9v4.5" stroke="#0b6fbf" stroke-width="1.4" fill="none"/></svg></span></a>
</section>

<section class="section contact">
  <div class="contact-card"></div>
  <div class="abs eyebrow center" style="top:137px">Contact us</div>
  <h2 class="abs title center" style="top:161px">Quick Inquiry</h2>
  <p class="abs copy center" style="top:198px">Have questions or ready to discuss your care? Contact us today.</p>

  <div class="field" style="left:342px;top:230px;width:256px"><span class="ico"><svg width="10" height="10" viewBox="0 0 10 10"><circle cx="5" cy="3" r="2.3" fill="#0b6fbf"/><path d="M1 10c0-3 2-4.5 4-4.5S9 7 9 10z" fill="#0b6fbf"/></svg></span><span>First Name*</span></div>
  <div class="field" style="left:612px;top:230px;width:255px"><span class="ico"><svg width="10" height="10" viewBox="0 0 10 10"><circle cx="5" cy="3" r="2.3" fill="#0b6fbf"/><path d="M1 10c0-3 2-4.5 4-4.5S9 7 9 10z" fill="#0b6fbf"/></svg></span><span>Last Name*</span></div>
  <div class="field" style="left:342px;top:279px;width:256px"><span class="ico"><svg width="10" height="10" viewBox="0 0 10 10"><path d="M2 1l2 2-1 1.5c.6 1.3 1.4 2 2.5 2.5L7 6l2 2-1.3 1.5C4.5 9 1 5.5.6 2.3z" fill="#0b6fbf"/></svg></span><span>Your Phone*</span></div>
  <div class="field" style="left:612px;top:279px;width:255px"><span class="ico"><svg width="11" height="9" viewBox="0 0 11 9"><rect width="11" height="9" rx="1" fill="#0b6fbf"/><path d="M1 1.5l4.5 3.5L10 1.5" stroke="#fff" fill="none"/></svg></span><span>Your Email*</span></div>
  <div class="field tall" style="left:342px;top:329px;width:525px"><span class="ico"><svg width="11" height="10" viewBox="0 0 11 10"><path d="M1 1h9v6H5L2.5 9V7H1z" fill="#0b6fbf"/></svg></span><span>Your Message</span></div>

  <a class="btn outline" href="#" style="left:531px;top:435px;width:137px"><span>Submit now</span><span class="arrow"><svg width="12" height="12" viewBox="0 0 12 12"><path d="M3 9L9 3M4.5 3H9v4.5" stroke="#0b6fbf" stroke-width="1.4" fill="none"/></svg></span></a>
</section>

<footer class="section site-footer">
  <div class="brand" style="left:470px;top:66px"><span class="dot" style="width:44px;height:44px"></span>DR. MATEUS VILHENA</div>
  <nav class="foot-nav">
    <a href="#">Home</a><a href="#">About</a><a href="#">Our Approach</a><a href="#">3D Planning</a><a href="#">Pre-Procedure</a><a href="#">Postoperative Care</a><a href="#">Our Commitment</a><a href="#">Contact</a>
  </nav>
  <div class="info" style="left:198px"><span class="ring"><svg width="14" height="11" viewBox="0 0 14 11"><rect width="14" height="11" rx="1.5" fill="#fff"/><path d="M1.5 2l5.5 4 5.5-4" stroke="#0b6fbf" stroke-width="1.2" fill="none"/></svg></span><div><b>EMAIL</b><span>info@drmateusvilhena.com</span></div></div>
  <div class="divider" style="left:437px"></div>
  <div class="info" style="left:476px"><span class="ring"><svg width="12" height="15" viewBox="0 0 12 15"><path d="M6 0a6 6 0 016 6c0 4-6 9-6 9S0 10 0 6a6 6 0 016-6z" fill="#fff"/><circle cx="6" cy="6" r="2.2" fill="#0b6fbf"/></svg></span><div><b>ADDRESS</b><span>45, Rua das Acácias, State XY 100200</span></div></div>
  <div class="divider" style="left:773px"></div>
  <div class="info" style="left:808px"><span class="ring"><svg width="13" height="13" viewBox="0 0 10 10"><path d="M2 1l2 2-1 1.5c.6 1.3 1.4 2 2.5 2.5L7 6l2 2-1.3 1.5C4.5 9 1 5.5.6 2.3z" fill="#fff"/></svg></span><div><b>PHONE</b><span>(555) 010-4821</span></div></div>
  <div class="foot-rule"></div>
  <p class="copyright">© 2025 DR. MATEUS VILHENA. All Rights Reserved.</p>
</footer>

</body>
</html>
```